Brixtondel - eCommerce Design and Shopify Theme customisation

eCommerce Website Design - firstly with mockups then once we have chosen the design the successful designer will need to choose, purchase and customise a Shopify theme to match the design. We have a logo already designed and now want to create our web presence based on carrying up to 50 products on our website.
Target Market(s)
UK Pet Owners
Industry/Entity Type
Pet Shop
Requirements
Must have
- Design must be achievable using a customised Shopify theme - the successful designer will be responsible for the delivery of a working theme on our shopify website.
Should not have
- should not look cheap or have designs that aren't compatible or achievable with Shopify

```html
<!DOCTYPE html>
<html lang="en">
<head>
<meta charset="utf-8">
<title>Brixtondel – Pet Shop</title>
<link rel="stylesheet" href="https://fonts.googleapis.com/css2?family=Lato:wght@400;700;900&display=swap">
<style>
:root{
  --cream:#fcf6e4;
  --cream-deep:#f6ecd0;
  --yellow:#d6b13b;
  --yellow-soft:#e3c55a;
  --dark:#323232;
  --darker:#262626;
  --grey:#8d8d8d;
  --text:#2b2b2b;
  --muted:#6b6b6b;
  --red:#c51d1d;
  --white:#ffffff;
}
*{box-sizing:border-box;margin:0;padding:0}
html,body{width:1200px;height:4265px;overflow:hidden}
body{position:relative;background:var(--cream);font-family:"Lato",sans-serif;color:var(--text)}
.abs{position:absolute}
.photo{position:absolute}
.btn{position:absolute;display:flex;align-items:center;justify-content:center;border-radius:30px;font-size:15px;font-weight:700}
.btn-yellow{background:var(--yellow);color:var(--dark)}
.btn-dark{background:var(--dark);color:var(--white)}

/* header */
.topbar{position:absolute;left:0;top:0;width:1200px;height:108px;background:var(--white)}
.phone{position:absolute;left:85px;top:46px;font-size:15px;font-weight:700;display:flex;align-items:center;gap:10px}
.brand{position:absolute;left:520px;top:20px;width:160px;text-align:center}
.brand-mark{width:44px;height:44px;border-radius:50%;background:var(--yellow);margin:0 auto 4px}
.brand-name{font-size:22px;font-weight:900;color:var(--dark)}
.header-icons{position:absolute;right:85px;top:44px;display:flex;gap:26px;align-items:center;font-size:14px}
.mainnav{position:absolute;left:0;top:108px;width:1200px;height:48px;background:var(--dark)}
.mainnav ul{list-style:none;display:flex;justify-content:center;height:48px}
.mainnav li{color:var(--white);font-size:15px;padding:0 34px;line-height:48px}
.mainnav li.active{background:var(--grey)}

/* hero */
.hero{position:absolute;left:0;top:156px;width:1200px;height:475px;background:var(--yellow)}
.hero-kicker{position:absolute;left:85px;top:150px;font-size:22px;font-weight:700;color:var(--dark)}
.hero-title{position:absolute;left:85px;top:178px;font-size:40px;font-weight:900;color:var(--dark)}
.hero-text{position:absolute;left:85px;top:232px;width:360px;font-size:14px;line-height:20px;color:var(--dark)}
.hero .photo{left:526px;top:20px;width:580px;height:420px;border-radius:12px;background:radial-gradient(ellipse at 50% 55%,#e8c47a 0%,#c9913f 45%,rgba(214,177,59,0) 75%)}

/* category panels */
.cat-photo{left:0;top:631px;width:600px;height:475px;background:linear-gradient(160deg,#e5e3e0,#cfc9c1 55%,#b8aea2)}
.dog-photo{left:600px;top:1106px;width:600px;height:475px;background:linear-gradient(150deg,#c9b59a,#8a6b4d 55%,#5c4634)}
.category{position:absolute;width:600px;height:475px;text-align:center}
.category .icon{width:56px;height:46px;margin:0 auto;border-radius:8px}
.category h2{font-size:34px;font-weight:700;margin-top:8px}
.category p{width:300px;margin:8px auto 0;font-size:14px;line-height:20px;color:var(--muted)}
.category .shop{position:relative;width:190px;height:48px;margin:16px auto 0;border-radius:30px;background:var(--yellow);font-size:14px;font-weight:700;line-height:48px}
.category .packs{width:320px;height:130px;margin:18px auto 0;border-radius:8px}

/* featured */
.section-title{position:absolute;width:1200px;text-align:center;font-size:28px;font-weight:700}
.tabs{position:absolute;left:0;top:1690px;width:1200px;display:flex;justify-content:center;gap:28px;font-size:14px}
.tabs .on{color:var(--yellow);font-weight:700}
.arrows{position:absolute;display:flex;gap:8px}
.arrow{width:34px;height:34px;border-radius:50%;border:2px solid var(--grey);display:flex;align-items:center;justify-content:center}
.arrow.next{border-color:var(--yellow)}
.product{position:absolute;top:1731px;width:255px;text-align:center}
.product .frame{height:273px;background:var(--white);border:1px solid #dcdcdc;display:flex;align-items:center;justify-content:center}
.product .pack{width:120px;height:190px;border-radius:6px}
.product .name{margin-top:14px;font-size:14px;color:var(--muted)}
.product .old{font-size:13px;color:var(--muted);text-decoration:line-through;margin-top:4px}
.product .price{font-size:19px;font-weight:900;color:var(--red);margin-top:2px}

/* promo */
.promo{position:absolute;left:0;top:2237px;width:1200px;height:592px;background:linear-gradient(90deg,var(--cream-deep),#f3e6c4)}
.promo .photo{left:0;top:120px;width:600px;height:360px;border-radius:10px;background:linear-gradient(120deg,#6ea84a,#b8d38d 40%,#d9c7a5 70%,rgba(243,230,196,0))}
.promo .faint{left:560px;top:0;width:640px;height:592px;background:radial-gradient(ellipse at 60% 50%,rgba(220,190,140,.45),rgba(243,230,196,0) 70%)}
.promo h3{position:absolute;left:654px;top:234px;font-size:32px;font-weight:400}
.promo .deal{position:absolute;left:654px;top:276px;font-size:22px;font-weight:700;color:var(--red)}
.promo p{position:absolute;left:654px;top:318px;width:330px;font-size:14px;line-height:20px}

/* blogs / testimonials */
.blogs-title{position:absolute;left:200px;top:2910px;font-size:34px;font-weight:700}
.post{position:absolute;left:80px;width:470px;height:160px}
.post .photo{left:0;top:0;width:200px;height:156px}
.post h4{position:absolute;left:225px;top:4px;font-size:17px;font-weight:700}
.post .date{position:absolute;left:225px;top:30px;font-size:13px;color:var(--muted)}
.post p{position:absolute;left:225px;top:54px;width:240px;font-size:13px;line-height:19px;color:var(--muted)}
.post .more{position:absolute;left:225px;top:130px;font-size:13px;color:var(--muted);text-decoration:underline}
.testimonials{position:absolute;left:597px;top:2891px;width:520px;height:535px;background:var(--cream-deep);text-align:center}
.testimonials h2{font-size:34px;font-weight:700;margin-top:38px}
.avatar{width:96px;height:96px;border-radius:50%;margin:36px auto 0;background:linear-gradient(160deg,#c99a7a,#8b5a3c);border:4px solid var(--white)}
.testimonials .who{font-size:19px;font-weight:700;margin-top:14px}
.testimonials .role{font-size:13px;color:var(--yellow);margin-top:2px}
.testimonials .quote{width:330px;margin:12px auto 0;font-size:13px;line-height:19px;color:var(--muted);position:relative}
.qmark{position:absolute;top:-4px;font-size:34px;font-weight:900;color:var(--dark);line-height:34px}
.stars{color:var(--yellow);font-size:17px;letter-spacing:2px;margin-top:10px}
.dots{display:flex;justify-content:center;gap:7px;margin-top:10px}
.dots span{width:7px;height:7px;border-radius:50%;background:#bdbdbd}
.dots span.on{background:var(--yellow)}

/* perks */
.perk{position:absolute;top:3537px;width:327px;height:142px;display:flex;align-items:center;padding-left:38px;gap:22px;color:var(--white)}
.perk.dark{background:var(--dark)}
.perk.gold{background:var(--yellow)}
.perk h5{font-size:17px;font-weight:700}
.perk p{font-size:13px;margin-top:4px}

/* newsletter */
.newsletter-title{position:absolute;left:0;top:3728px;width:1200px;text-align:center;font-size:32px;font-weight:700}
.newsletter-sub{position:absolute;left:0;top:3772px;width:1200px;text-align:center;font-size:13px;line-height:18px;color:var(--muted)}
.subscribe{position:absolute;left:353px;top:3818px;width:480px;height:38px;background:var(--white);border-radius:20px;border:1px solid #e2d8bf}
.subscribe span{position:absolute;left:22px;top:10px;font-size:13px;color:#9a9a9a}
.subscribe .send{position:absolute;right:-1px;top:-1px;width:60px;height:38px;border-radius:20px;background:var(--yellow);display:flex;align-items:center;justify-content:center}

/* footer */
.footer{position:absolute;left:0;top:3903px;width:1200px;height:305px;background:var(--dark);color:var(--white)}
.foot-brand{position:absolute;left:82px;top:40px;display:flex;align-items:center;gap:10px}
.foot-brand .dot{width:40px;height:40px;border-radius:50%;background:var(--yellow)}
.foot-brand span{font-size:22px;font-weight:900}
.contact{position:absolute;left:82px;top:112px;list-style:none;font-size:14px;line-height:24px}
.contact li{display:flex;align-items:flex-start;gap:10px}
.contact svg{margin-top:6px;flex:none}
.col{position:absolute;top:64px}
.col h6{font-size:17px;font-weight:700;margin-bottom:16px}
.col ul{list-style:none;font-size:14px;line-height:25px}
.col ul li::before{content:"›";margin-right:10px;color:#bbb}
.social li::before{content:none!important}
.social li{display:flex;align-items:center;gap:12px}
.social .ring{width:16px;height:16px;border-radius:50%}
.bottombar{position:absolute;left:0;top:4208px;width:1200px;height:57px;background:var(--cream)}
.bottombar p{position:absolute;left:82px;top:20px;font-size:13px;color:var(--muted)}
.cards{position:absolute;right:82px;top:16px;display:flex;gap:8px}
.cards span{width:44px;height:26px;border-radius:3px;border:1px solid #cfc6b0}
</style>
</head>
<body>

<header class="topbar">
  <div class="phone">
    <svg width="18" height="18" viewBox="0 0 24 24"><circle cx="12" cy="12" r="10.5" fill="none" stroke="#323232" stroke-width="2"/><path d="M8.5 7.5l2 2-1 1.5c.8 1.6 2 2.8 3.5 3.5l1.5-1 2 2-1.5 1.5c-3.5-.5-6.5-3.5-7-7z" fill="#323232"/></svg>
    0116 496 0172
  </div>
  <div class="brand">
    <div class="brand-mark"></div>
    <div class="brand-name">Brixtondel</div>
  </div>
  <div class="header-icons">
    <svg width="18" height="18" viewBox="0 0 24 24"><circle cx="10" cy="10" r="6.5" fill="none" stroke="#323232" stroke-width="2.4"/><path d="M15 15l6 6" stroke="#323232" stroke-width="2.6"/></svg>
    <svg width="18" height="18" viewBox="0 0 24 24"><circle cx="12" cy="8" r="4.5" fill="none" stroke="#323232" stroke-width="2"/><path d="M4 21c1-5 15-5 16 0" fill="none" stroke="#323232" stroke-width="2"/></svg>
    <span style="display:flex;align-items:center;gap:6px"><svg width="20" height="18" viewBox="0 0 24 22"><path d="M1 2h4l3 12h12l3-9H7" fill="none" stroke="#323232" stroke-width="2"/><circle cx="9" cy="19" r="2" fill="#323232"/><circle cx="19" cy="19" r="2" fill="#323232"/></svg>(2)</span>
  </div>
</header>

<nav class="mainnav">
  <ul>
    <li class="active">Home</li><li>Dog</li><li>Cat</li><li>Shop</li><li>Blog</li><li>Contact us</li>
  </ul>
</nav>

<section class="hero">
  <div class="hero-kicker">Welcome To</div>
  <h1 class="hero-title">All Pet Products</h1>
  <p class="hero-text">Lorem Ipsum is simply dummy text of the printing and typesetting industry.</p>
  <div class="btn btn-dark" style="left:85px;top:280px;width:190px;height:50px">Read More</div>
  <div class="photo" role="img" aria-label="Golden retriever, collie puppy and ginger cat lying beside bowls of pet food"></div>
</section>

<div class="photo cat-photo" role="img" aria-label="Fluffy white cat lying on a table beside an orchid plant"></div>
<section class="category" style="left:600px;top:631px;padding-top:82px">
  <div class="icon" role="img" aria-label="Cat head icon" style="background:#9a9a9a"></div>
  <h2>Cat Products</h2>
  <p>Lorem Ipsum is simply dummy text of the printing and typesetting industry.</p>
  <div class="shop">Shop Now&gt;&gt;</div>
  <div class="packs" role="img" aria-label="Row of colourful cat food pouches" style="background:linear-gradient(90deg,#c94e6a,#6ab04c,#e4c24a,#3f8fc7,#d2506a)"></div>
</section>

<section class="category" style="left:0;top:1106px;padding-top:82px">
  <div class="icon" role="img" aria-label="Dog head icon" style="background:var(--yellow)"></div>
  <h2>Dog Products</h2>
  <p>Lorem Ipsum is simply dummy text of the printing and typesetting industry.</p>
  <div class="shop">Shop Now&gt;&gt;</div>
  <div class="packs" role="img" aria-label="Group of dog food tins" style="background:linear-gradient(90deg,#d45f7a,#7cb24a,#5c8d3a,#d45f7a)"></div>
</section>
<div class="photo dog-photo" role="img" aria-label="Small long-haired terrier running towards the camera"></div>

<h2 class="section-title" style="top:1632px">Feature Products</h2>
<div class="tabs"><span class="on">ALL</span><span>Cats</span><span>Dogs</span><span>Other</span></div>
<div class="arrows" style="right:80px;top:1672px">
  <div class="arrow"><svg width="12" height="12" viewBox="0 0 12 12"><path d="M8 1L3 6l5 5" fill="none" stroke="#8d8d8d" stroke-width="2"/></svg></div>
  <div class="arrow next"><svg width="12" height="12" viewBox="0 0 12 12"><path d="M4 1l5 5-5 5" fill="none" stroke="#d6b13b" stroke-width="2"/></svg></div>
</div>

<div class="product" style="left:82px">
  <div class="frame"><div class="pack" role="img" aria-label="Bag of dog food" style="background:linear-gradient(#2f6db3,#e9913a)"></div></div>
  <div class="name">Product Name</div><div class="old">$00.00</div><div class="price">$00.00</div>
</div>
<div class="product" style="left:336px">
  <div class="frame"><div class="pack" role="img" aria-label="Bag of chicken cat food" style="background:linear-gradient(#d9b46a,#b9832f)"></div></div>
  <div class="name">Product Name</div><div class="old">$00.00</div><div class="price">$00.00</div>
</div>
<div class="product" style="left:600px">
  <div class="frame"><div class="pack" role="img" aria-label="Tin of pet food" style="width:110px;height:170px;background:linear-gradient(90deg,#c8c8c8,#e8b23a 40%,#2d4fa1)"></div></div>
  <div class="name">Product Name</div><div class="old">$00.00</div><div class="price">$00.00</div>
</div>
<div class="product" style="left:862px">
  <div class="frame"><div class="pack" role="img" aria-label="Small tin of cat food" style="width:140px;height:110px;background:linear-gradient(#d5d5d5,#e89a3a 40%,#7b3f9b)"></div></div>
  <div class="name">Product Name</div><div class="old">$00.00</div><div class="price">$00.00</div>
</div>
<div class="btn btn-yellow" style="left:520px;top:2106px;width:185px;height:50px">Browse All</div>

<section class="promo">
  <div class="photo faint" role="img" aria-label="Faded photo of a cat and dog resting together"></div>
  <div class="photo" role="img" aria-label="Stack of dog and cat food bags and a fresh food roll"></div>
  <h3>Save up to 40%</h3>
  <div class="deal">$120.200</div>
  <p>Lorem Ipsum is simply dummy text of the printing and typesetting industry.</p>
  <div class="btn btn-yellow" style="left:654px;top:360px;width:185px;height:48px">Shop Now &gt;&gt;</div>
</section>

<h2 class="blogs-title">Blogs</h2>
<article class="post" style="top:2985px">
  <div class="photo" role="img" aria-label="Ginger cat eating from a bowl" style="background:linear-gradient(135deg,#c98a4e,#7a5337)"></div>
  <h4>Blog Title Heading 01</h4>
  <div class="date">29 April, 2019</div>
  <p>Lorem Ipsum is simply dummy text of the printing typesetting industry. Ipsum has industryin the standard dummy.</p>
  <div class="more">Read More</div>
</article>
<article class="post" style="top:3184px">
  <div class="photo" role="img" aria-label="Golden puppy beside a pile of dry food" style="background:linear-gradient(135deg,#e3c07a,#b37b3a)"></div>
  <h4>Blog Title Heading 01</h4>
  <div class="date">28April, 2019</div>
  <p>Lorem Ipsum is simply dummy text of the printing typesetting industry. Ipsum has industryin the standard dummy.</p>
  <div class="more">Read More</div>
</article>
<div class="arrows" style="left:268px;top:3378px">
  <div class="arrow"><svg width="12" height="12" viewBox="0 0 12 12"><path d="M8 1L3 6l5 5" fill="none" stroke="#8d8d8d" stroke-width="2"/></svg></div>
  <div class="arrow next"><svg width="12" height="12" viewBox="0 0 12 12"><path d="M4 1l5 5-5 5" fill="none" stroke="#d6b13b" stroke-width="2"/></svg></div>
</div>

<section class="testimonials">
  <h2>Testimonials</h2>
  <div class="avatar" role="img" aria-label="Portrait photo of the reviewer"></div>
  <div class="who">Clara Whitby</div>
  <div class="role">Director</div>
  <div class="quote">
    <span class="qmark" style="left:-26px">“</span>
    Lorem Ipsum is simply dummy text of the printing typesetting industry. Ipsum has been theindustry in the standard dummy.
    <span class="qmark" style="right:-26px;top:30px">”</span>
  </div>
  <div class="stars">★★★★★</div>
  <div class="dots"><span></span><span class="on"></span><span></span></div>
</section>

<div class="perk dark" style="left:80px">
  <svg width="44" height="30" viewBox="0 0 44 30"><path d="M2 4h24v18H2zM26 10h9l6 7v5H26z" fill="none" stroke="#fff" stroke-width="2"/><circle cx="10" cy="24" r="3.5" fill="#323232" stroke="#fff" stroke-width="2"/><circle cx="33" cy="24" r="3.5" fill="#323232" stroke="#fff" stroke-width="2"/></svg>
  <div><h5>Free Shipping Worldwide</h5><p>On Order<br>Over $1507 Days a week</p></div>
</div>
<div class="perk gold" style="left:435px">
  <svg width="36" height="36" viewBox="0 0 36 36"><path d="M6 20v-4a12 12 0 0124 0v4" fill="none" stroke="#fff" stroke-width="2.4"/><rect x="3" y="18" width="7" height="11" rx="2" fill="#fff"/><rect x="26" y="18" width="7" height="11" rx="2" fill="#fff"/></svg>
  <div><h5>24/7 Customer Service</h5><p>Call us 24/7<br>0116 496 0172</p></div>
</div>
<div class="perk dark" style="left:790px">
  <svg width="36" height="36" viewBox="0 0 36 36"><path d="M4 18L18 4h13v13L17 31z" fill="none" stroke="#fff" stroke-width="2.2"/><circle cx="25" cy="11" r="2.5" fill="#fff"/></svg>
  <div><h5>Save 15%</h5><p>with the Brixtondel Card</p></div>
</div>

<h2 class="newsletter-title">Subscribe To Our Newsletter</h2>
<p class="newsletter-sub">Subscribe to our newsletter so we can spam you<br>with offers and discounts.</p>
<div class="subscribe">
  <span>Your E-Mail</span>
  <div class="send"><svg width="20" height="18" viewBox="0 0 20 18"><path d="M1 8L19 1l-5 16-4-6z" fill="#fff"/></svg></div>
</div>

<footer class="footer">
  <div class="foot-brand"><div class="dot"></div><span>Brixtondel</span></div>
  <ul class="contact">
    <li><svg width="12" height="14" viewBox="0 0 12 14"><path d="M6 0a5 5 0 015 5c0 4-5 9-5 9S1 9 1 5a5 5 0 015-5z" fill="#fff"/><circle cx="6" cy="5" r="2" fill="#323232"/></svg><span>48 Alder Lane<br>Northfield, UK</span></li>
    <li><svg width="12" height="12" viewBox="0 0 12 12"><path d="M2 1l2.5 2.5-1 1.5c.8 1.6 1.8 2.6 3.5 3.5l1.5-1L11 10l-1.5 1.5C5 11 1 7 .5 2.5z" fill="#fff"/></svg>(44) 1632-960-414</li>
    <li><svg width="12" height="10" viewBox="0 0 12 10"><rect width="12" height="10" fill="#fff"/><path d="M0 0l6 5 6-5" fill="none" stroke="#323232" stroke-width="1.3"/></svg>sales@brixtondel.com</li>
  </ul>
  <div class="col" style="left:408px">
    <h6>Quick Link</h6>
    <ul><li>My Account</li><li>Cart Page</li><li>Personal info</li><li>wishlist</li><li>Gifts</li><li>Terms and Conditions</li></ul>
  </div>
  <div class="col" style="left:638px">
    <h6>Quick link</h6>
    <ul><li>Home</li><li>Dog</li><li>Cat</li><li>Shop</li><li>Blog</li><li>Contact us</li></ul>
  </div>
  <div class="col" style="left:858px">
    <h6>Follow us on Social Media</h6>
    <ul class="social">
      <li><span class="ring" style="background:#3b5998"></span>Pawbook</li>
      <li><span class="ring" style="background:#c1355a"></span>Snapgram</li>
      <li><span class="ring" style="background:#29a9e1"></span>Chirper</li>
      <li><span class="ring" style="background:#0e76a8"></span>Linkwork</li>
    </ul>
  </div>
</footer>

<div class="bottombar">
  <p>Copyright © 2019 Brixtondel. All Rights Reserved.</p>
  <div class="cards">
    <span style="background:#1a3f8f"></span><span style="background:#e9e2d0"></span><span style="background:#f1f1f1"></span><span style="background:#6a9bd1"></span>
  </div>
</div>

</body>
</html>
```